Need UI Design for HRIS/Company Employee Portal

Currently have a custom built system that we hire and use as our employee database and employee portal for everyone in our company. The software has evolved dramatically and needs to be completely user friendly and aesthetically pleasing. Attached are a few ideas and pages we already have. Please make 5 designs for the 5 different pages below. Would need all specifications of content used, color code, font/typography, icons used, etc. We can pretty much pull any information from anywhere we have for example, employee photo, address, DOB, Hire date, Title, ETC.

-Company Staff/Admin Welcome Page
- We want quick shortcuts/buttons or icons for staff functions, such as terminate, hire, information change, reports, etc
-Employee Profile Welcome Page
- We want quick shortcuts/buttons or icons for direct deposit, time off request, information change, pay stubs
-List of Applications/Candidates Page
-Profile Search Page
-Manage Inventory

Target Market(s)

Employees

Industry/Entity Type

It Company

Coding

Coded - Design and coding required

Number of Pages Required

5+ page

Font styles to use
Sans Serif

Requirements
Must have
• Must be professional! Aesthetics, Icons, Easy User Interface, Modern New technology look, can be responsive to mobile
Should not have
• Nothing old school

```html
<!DOCTYPE html>
<html lang="en">
<head>
<meta charset="utf-8">
<title>Northgate Staff Services – Employee Portal</title>
<link href="https://fonts.googleapis.com/css2?family=Open+Sans:wght@400;600;700&display=swap" rel="stylesheet">
<style>
  :root {
    --brand-blue: #4d7ee3;
    --brand-blue-dark: #3261cc;
    --page-bg: #e6e6e6;
    --surface: #ffffff;
    --text: #333333;
    --text-muted: #8a8a8a;
    --line: #e2e2e2;
    --alert: #e00000;
    --logo-blue: #3d56a8;
  }
  * { box-sizing: border-box; margin: 0; padding: 0; }
  html, body { width: 1200px; height: 1050px; overflow: hidden; }
  body {
    background: var(--page-bg);
    font-family: "Open Sans", Arial, sans-serif;
    color: var(--text);
    position: relative;
  }
  .icon-defs { position: absolute; width: 0; height: 0; }

  /* Header */
  .site-header { position: absolute; top: 0; left: 0; width: 1200px; height: 152px; }
  .brand { position: absolute; left: 28px; top: 66px; display: flex; align-items: center; gap: 14px; }
  .brand-mark { width: 30px; height: 30px; background: var(--logo-blue); }
  .brand-name { font-size: 17px; font-weight: 700; color: var(--logo-blue); letter-spacing: .3px; }
  .site-search { position: absolute; left: 770px; top: 58px; display: flex; height: 50px; }
  .site-search-field {
    width: 275px; height: 50px; background: var(--surface);
    font-size: 20px; color: var(--text); padding: 0 16px;
    display: flex; align-items: center;
  }
  .icon-button {
    width: 52px; height: 50px; background: var(--brand-blue);
    display: flex; align-items: center; justify-content: center;
  }
  .logout-button { position: absolute; left: 1122px; top: 58px; width: 50px; }

  /* Navigation */
  .main-nav {
    position: absolute; top: 152px; left: 0; width: 1200px; height: 48px;
    background: var(--brand-blue); display: flex; align-items: center;
    padding-left: 28px; gap: 38px;
  }
  .main-nav a { color: #fff; text-decoration: none; font-size: 19px; font-weight: 400; }

  /* Filters */
  .filters { position: absolute; top: 234px; left: 28px; height: 50px; }
  .filter-name { position: absolute; left: 0; display: flex; }
  .filter-name .field { width: 189px; }
  .field {
    height: 50px; background: var(--surface); display: flex; align-items: center;
    padding-left: 14px; font-size: 17px; color: #555;
  }
  .filter-name .icon-button { width: 50px; }
  .reset-button {
    position: absolute; left: 258px; width: 100px; height: 50px;
    background: var(--brand-blue); color: #fff; font-size: 21px;
    display: flex; align-items: center; justify-content: center;
  }
  .select { position: absolute; width: 216px; display: flex; }
  .select .field { flex: 1; }
  .select .icon-button { width: 50px; }
  .select-job { left: 377px; }
  .select-status { left: 611px; }
  .select-office { left: 845px; }

  /* Table */
  .staff-table {
    position: absolute; top: 320px; left: 28px; width: 1144px;
    border-collapse: collapse; table-layout: fixed; background: var(--surface);
  }
  .staff-table th {
    height: 50px; background: var(--brand-blue); color: #fff;
    font-size: 16px; font-weight: 600; text-align: left; padding-left: 11px;
    border-right: 1px solid #6f97ea;
  }
  .staff-table td {
    height: 64px; font-size: 14px; padding: 0 0 0 11px;
    border-right: 1px solid var(--line); border-bottom: 1px solid var(--line);
    vertical-align: middle; line-height: 20px; white-space: nowrap;
  }
  .staff-table th:last-child, .staff-table td:last-child { border-right: 0; }
  .staff-table .centered { text-align: center; padding-left: 0; }
  .phone-line { display: flex; align-items: center; gap: 6px; }
  .phone-line svg { flex: none; }
  .status-expired, .note-alert { color: var(--alert); }

  /* Pagination */
  .pagination {
    position: absolute; top: 884px; left: 28px; width: 1144px; height: 50px;
    background: var(--brand-blue); display: flex; align-items: center; color: #fff;
  }
  .page-arrow {
    width: 50px; height: 50px; background: var(--brand-blue-dark);
    display: flex; align-items: center; justify-content: center; border-right: 1px solid var(--brand-blue);
  }
  .page-numbers { display: flex; align-items: center; height: 50px; margin: 0 12px; }
  .page-numbers span { font-size: 18px; font-weight: 600; padding: 0 6px; line-height: 50px; }
  .page-numbers .current { background: var(--brand-blue-dark); }
  .page-summary { margin-left: auto; padding-right: 22px; font-size: 17px; font-weight: 700; }

  /* Footer */
  .site-footer {
    position: absolute; top: 966px; left: 28px; width: 1144px; height: 50px;
    background: var(--surface); display: flex; align-items: center; padding: 0 16px;
  }
  .copyright { font-size: 19px; font-weight: 700; color: var(--text-muted); }
  .footer-links { margin-left: auto; display: flex; gap: 42px; }
  .footer-links a { color: var(--brand-blue); font-size: 21px; font-weight: 700; text-decoration: none; }
</style>
</head>
<body>

<svg class="icon-defs" aria-hidden="true">
  <symbol id="icon-search" viewBox="0 0 24 24"><circle cx="10" cy="10" r="6.5" fill="none" stroke="#fff" stroke-width="2.6"/><line x1="15" y1="15" x2="21" y2="21" stroke="#fff" stroke-width="3" stroke-linecap="round"/></symbol>
  <symbol id="icon-power" viewBox="0 0 24 24"><path d="M7.5 6.5a8 8 0 1 0 9 0" fill="none" stroke="#fff" stroke-width="2.4" stroke-linecap="round"/><line x1="12" y1="3" x2="12" y2="12" stroke="#fff" stroke-width="2.4" stroke-linecap="round"/></symbol>
  <symbol id="icon-caret" viewBox="0 0 24 24"><path d="M3 5h18L12 21z" fill="#fff"/></symbol>
  <symbol id="icon-phone" viewBox="0 0 24 24"><path d="M6.6 10.8a15 15 0 0 0 6.6 6.6l2.2-2.2a1 1 0 0 1 1-.25 11.4 11.4 0 0 0 3.6.57 1 1 0 0 1 1 1V20a1 1 0 0 1-1 1A17 17 0 0 1 3 4a1 1 0 0 1 1-1h3.5a1 1 0 0 1 1 1c0 1.25.2 2.45.57 3.57a1 1 0 0 1-.25 1z" fill="#222"/></symbol>
  <symbol id="icon-mobile" viewBox="0 0 24 24"><rect x="6" y="1.5" width="12" height="21" rx="2" fill="none" stroke="#222" stroke-width="2"/><line x1="10" y1="19" x2="14" y2="19" stroke="#222" stroke-width="1.6"/></symbol>
  <symbol id="icon-first" viewBox="0 0 24 24"><rect x="3" y="3" width="3" height="18" fill="#fff"/><path d="M21 3v18L8 12z" fill="#fff"/></symbol>
  <symbol id="icon-prev" viewBox="0 0 24 24"><path d="M19 3v18L5 12z" fill="#fff"/></symbol>
  <symbol id="icon-next" viewBox="0 0 24 24"><path d="M5 3v18l14-9z" fill="#fff"/></symbol>
  <symbol id="icon-last" viewBox="0 0 24 24"><path d="M3 3v18l13-9z" fill="#fff"/><rect x="18" y="3" width="3" height="18" fill="#fff"/></symbol>
</svg>

<header class="site-header">
  <div class="brand">
    <span class="brand-mark"></span>
    <span class="brand-name">NORTHGATE STAFF SERVICES, INC.</span>
  </div>
  <div class="site-search">
    <div class="site-search-field">Search</div>
    <div class="icon-button"><svg width="24" height="24"><use href="#icon-search"/></svg></div>
  </div>
  <div class="icon-button logout-button"><svg width="26" height="26"><use href="#icon-power"/></svg></div>
</header>

<nav class="main-nav">
  <a href="#">Home</a>
  <a href="#">Personal Licenses</a>
  <a href="#">Forms\Requests</a>
  <a href="#">Team Contacts</a>
  <a href="#">Benefits</a>
  <a href="#">Training</a>
  <a href="#">Equipment</a>
  <a href="#">Help</a>
</nav>

<section class="filters">
  <div class="filter-name">
    <div class="field">Name</div>
    <div class="icon-button"><svg width="22" height="22"><use href="#icon-search"/></svg></div>
  </div>
  <div class="reset-button">Reset</div>
  <div class="select select-job"><div class="field">JOB</div><div class="icon-button"><svg width="22" height="22"><use href="#icon-caret"/></svg></div></div>
  <div class="select select-status"><div class="field">STATUS</div><div class="icon-button"><svg width="22" height="22"><use href="#icon-caret"/></svg></div></div>
  <div class="select select-office"><div class="field">OFFICE</div><div class="icon-button"><svg width="22" height="22"><use href="#icon-caret"/></svg></div></div>
</section>

<table class="staff-table">
  <colgroup>
    <col style="width:94px"><col style="width:125px"><col style="width:173px"><col style="width:141px">
    <col style="width:186px"><col style="width:87px"><col style="width:166px"><col style="width:172px">
  </colgroup>
  <thead>
    <tr><th>Created</th><th>Appointment</th><th>Name</th><th>Phone</th><th>Address</th><th>Status</th><th>Notes</th><th>Job Title</th></tr>
  </thead>
  <tbody>
    <tr><td>27 Mar 16</td><td class="centered">29 Mar 16</td><td>Sam Porter</td><td><div class="phone-line"><svg width="15" height="15"><use href="#icon-phone"/></svg>212-480-7315</div><div class="phone-line"><svg width="15" height="16"><use href="#icon-mobile"/></svg>07700900432</div></td><td>18 Birch Lane<br>NY 10021</td><td class="centered">Active</td><td></td><td>Un-Armed Guard</td></tr>
    <tr><td>27 Mar 16</td><td class="centered">29 Mar 16</td><td>Sam Porter</td><td><div class="phone-line"><svg width="15" height="15"><use href="#icon-phone"/></svg>212-480-7315</div><div class="phone-line"><svg width="15" height="16"><use href="#icon-mobile"/></svg>07700900432</div></td><td>18 Birch Lane<br>NY 10021</td><td class="centered">Active</td><td></td><td>Un-Armed Guard</td></tr>
    <tr><td>27 Mar 16</td><td class="centered">29 Mar 16</td><td>Sam Porter</td><td><div class="phone-line"><svg width="15" height="15"><use href="#icon-phone"/></svg>212-480-7315</div><div class="phone-line"><svg width="15" height="16"><use href="#icon-mobile"/></svg>07700900432</div></td><td>18 Birch Lane<br>NY 10021</td><td class="centered">Active</td><td></td><td>Un-Armed Guard</td></tr>
    <tr><td>27 Mar 16</td><td class="centered">29 Mar 16</td><td>Sam Porter</td><td><div class="phone-line"><svg width="15" height="15"><use href="#icon-phone"/></svg>212-480-7315</div><div class="phone-line"><svg width="15" height="16"><use href="#icon-mobile"/></svg>07700900432</div></td><td>18 Birch Lane<br>NY 10021</td><td class="centered">Active</td><td></td><td>Un-Armed Guard</td></tr>
    <tr><td>27 Mar 16</td><td class="centered">29 Mar 16</td><td>Sam Porter</td><td><div class="phone-line"><svg width="15" height="15"><use href="#icon-phone"/></svg>212-480-7315</div><div class="phone-line"><svg width="15" height="16"><use href="#icon-mobile"/></svg>07700900432</div></td><td>18 Birch Lane<br>NY 10021</td><td class="centered">Active</td><td></td><td>Un-Armed Guard</td></tr>
    <tr><td>27 Mar 16</td><td class="centered">29 Mar 16</td><td>Sam Porter</td><td><div class="phone-line"><svg width="15" height="15"><use href="#icon-phone"/></svg>212-480-7315</div><div class="phone-line"><svg width="15" height="16"><use href="#icon-mobile"/></svg>07700900432</div></td><td>18 Birch Lane<br>NY 10021</td><td class="centered status-expired">Expired</td><td class="note-alert">Invalid guard card!</td><td>Un-Armed Guard</td></tr>
    <tr><td>27 Mar 16</td><td class="centered">29 Mar 16</td><td>Sam Porter</td><td><div class="phone-line"><svg width="15" height="15"><use href="#icon-phone"/></svg>212-480-7315</div><div class="phone-line"><svg width="15" height="16"><use href="#icon-mobile"/></svg>07700900432</div></td><td>18 Birch Lane<br>NY 10021</td><td class="centered">Active</td><td></td><td>Un-Armed Guard</td></tr>
    <tr><td>27 Mar 16</td><td class="centered">29 Mar 16</td><td>Sam Porter</td><td><div class="phone-line"><svg width="15" height="15"><use href="#icon-phone"/></svg>212-480-7315</div><div class="phone-line"><svg width="15" height="16"><use href="#icon-mobile"/></svg>07700900432</div></td><td>18 Birch Lane<br>NY 10021</td><td class="centered">Active</td><td></td><td>Un-Armed Guard</td></tr>
  </tbody>
</table>

<nav class="pagination" aria-label="Pages">
  <div class="page-arrow"><svg width="26" height="26"><use href="#icon-first"/></svg></div>
  <div class="page-arrow"><svg width="22" height="22"><use href="#icon-prev"/></svg></div>
  <div class="page-numbers">
    <span class="current">1</span><span>2</span><span>3</span><span>4</span><span>5</span><span>6</span><span>7</span><span>8</span><span>9</span><span>10</span><span>…</span>
  </div>
  <div class="page-arrow"><svg width="22" height="22"><use href="#icon-next"/></svg></div>
  <div class="page-arrow"><svg width="26" height="26"><use href="#icon-last"/></svg></div>
  <div class="page-summary">12343 items in 634 Pages</div>
</nav>

<footer class="site-footer">
  <span class="copyright">© 2016&nbsp; NSS</span>
  <div class="footer-links"><a href="#">Legal</a><a href="#">Terms</a></div>
</footer>

</body>
</html>
```